Flyer overhaul from current flyers

I need to have our current flyers updated with a fresher look. We also need to have a new utility and real estate flyer created that will go along with the design of the new flyer. We are looking for new pictures, new overall design, same color scheme but would like to have the flyers more airy and inviting.

Target Market(s)

decision makers in the healthcare/utilty/banking/real estate sectors

Font styles to use
Other font styles liked:
• Logo is in Bell MT

Colors
0054AA
0677BA
7BADD7
CADEEF
E8F1F8

Requirements
Must have
• Close to what is currently on the existing flyers

```html
<!DOCTYPE html>
<html lang="en">
<head>
<meta charset="utf-8">
<title>Utility Collections Flyer</title>
<link href="https://fonts.googleapis.com/css2?family=Figtree:wght@400;500;600;700&display=swap" rel="stylesheet">
<style>
:root{
  --stage:#c4c4c4;
  --white:#ffffff;
  --ink:#1f2a33;
  --dark:#2a2a2c;
  --teal:#0e5b80;
  --blue:#0677BA;
  --navy:#0054AA;
  --sky:#7BADD7;
  --mist:#CADEEF;
  --pale:#E8F1F8;
  --night-a:#4a2f9a;
  --night-b:#1b1734;
  --storm-a:#1a1614;
  --storm-b:#6b5148;
}
*{box-sizing:border-box;margin:0;padding:0}
html,body{width:1200px;height:800px;overflow:hidden;background:var(--stage);font-family:"Figtree",sans-serif}
.flyer{position:absolute;top:52px;width:528px;height:683px;background:var(--white);overflow:hidden}
.flyer--services{left:54px}
.flyer--philosophy{left:626px}
.flyer__art{position:absolute;inset:0}
.brand{position:absolute;left:25px;top:30px;display:flex;align-items:center;gap:10px}
.brand__dot{width:44px;height:44px;border-radius:50%;background:var(--white)}
.brand__name{color:var(--white);font-weight:600;font-size:18px;line-height:1.1;letter-spacing:.5px}
.headline{position:absolute;right:28px;top:14px;text-align:right;color:var(--white)}
.headline__light{font-size:35px;font-weight:400;line-height:1.05}
.headline__bold{font-size:41px;font-weight:700;line-height:1.05}
.tagline{position:absolute;left:38px;top:520px;transform:rotate(-90deg);transform-origin:left top;color:var(--white);font-size:27px;font-weight:400;white-space:nowrap;letter-spacing:.5px}
.feature{position:absolute;display:flex;align-items:center;gap:12px}
.feature__icon{width:68px;height:68px;border-radius:50%;background:var(--dark);box-shadow:0 0 0 4px var(--white),0 0 0 5px #5c6e7a;flex:none}
.feature__text{font-size:10.8px;font-weight:600;color:var(--ink);line-height:1.28;white-space:nowrap}
.divider{position:absolute;border-top:1.5px dashed var(--teal);width:86px}
.services{position:absolute;left:340px;top:300px}
.section-title{color:var(--teal);font-weight:700;font-size:28px;line-height:1.05}
.services__rule{position:absolute;left:340px;top:366px;width:170px;border-top:1.5px dashed var(--teal)}
.services__rule::after{content:"";position:absolute;right:-2px;top:-4px;width:6px;height:6px;border-radius:50%;background:var(--teal)}
.service-list{position:absolute;left:340px;top:383px;list-style:none}
.service-list li{font-size:10.6px;color:var(--ink);height:16.4px;display:flex;align-items:center;gap:6px;font-weight:500;white-space:nowrap}
.tick{width:9px;height:9px;flex:none}
.call{position:absolute;left:288px;top:584px;width:222px;height:52px;border-radius:18px;background:var(--teal);display:flex;align-items:center;padding-left:14px;gap:8px;color:var(--white)}
.call__badge{width:36px;height:36px;border-radius:50%;background:var(--white);display:flex;align-items:center;justify-content:center;flex:none}
.call__label{font-size:11px;font-weight:700;line-height:1}
.call__number{font-size:20px;font-weight:700;line-height:1.1;white-space:nowrap}
.site{position:absolute;right:18px;top:645px;color:var(--white);font-size:18px;font-weight:700;white-space:nowrap}
.philosophy__title{position:absolute;left:46px;top:346px;color:var(--teal);font-weight:700;font-size:33px;line-height:1.12}
.philosophy__body{position:absolute;left:47px;top:431px;font-size:10.6px;line-height:13.45px;color:var(--ink);font-weight:500;white-space:nowrap}
</style>
</head>
<body>

<section class="flyer flyer--services">
  <svg class="flyer__art" width="528" height="683" viewBox="0 0 528 683">
    <defs>
      <linearGradient id="nightSky" x1="0" y1="0" x2="0" y2="1">
        <stop offset="0" stop-color="var(--night-a)"/>
        <stop offset="1" stop-color="var(--night-b)"/>
      </linearGradient>
      <radialGradient id="deepBlue" cx="0" cy="0.5" r="1">
        <stop offset="0" stop-color="var(--navy)"/>
        <stop offset="1" stop-color="#2a2f8a"/>
      </radialGradient>
    </defs>
    <rect width="528" height="370" fill="url(#nightSky)" role="img" aria-label="Photo of a downtown city skyline at night"/>
    <path d="M0,133 C110,128 200,175 265,245 C300,285 335,300 380,298 C440,296 490,300 528,318 L528,683 L0,683Z" fill="var(--white)"/>
    <path d="M185,190 C230,220 270,290 330,300 C320,310 280,300 250,275 C225,250 205,215 185,190Z" fill="var(--sky)"/>
    <rect x="318" y="296" width="210" height="302" fill="var(--pale)"/>
    <ellipse cx="0" cy="410" rx="186" ry="200" fill="url(#deepBlue)"/>
    <rect x="35" y="300" width="36" height="230" fill="#ffffff" opacity=".12"/>
    <g fill="var(--white)">
      <rect x="410" y="258" width="15" height="40"/>
      <rect x="433" y="236" width="15" height="62"/>
      <rect x="456" y="212" width="15" height="86"/>
      <rect x="479" y="194" width="15" height="104"/>
      <rect x="502" y="172" width="15" height="150"/>
    </g>
    <path d="M0,683 L0,672 C160,660 300,620 528,596 L528,683Z" fill="var(--dark)"/>
    <path d="M110,668 C200,660 260,640 300,632 C250,650 180,664 110,668Z" fill="var(--blue)"/>
  </svg>

  <div class="brand"><span class="brand__dot"></span><span class="brand__name">NORTHGATE<br>RECOVERY</span></div>
  <div class="headline"><div class="headline__light">Utility</div><div class="headline__bold">Collections</div></div>
  <div class="tagline">Forward Thinking</div>

  <div class="feature" style="left:20px;top:182px"><span class="feature__icon" role="img" aria-label="Friendly service icon"></span><span class="feature__text">A Friendly,<br>Professional<br>Approach</span></div>
  <div class="feature" style="left:100px;top:249px"><span class="feature__icon" role="img" aria-label="Online payment icon"></span><span class="feature__text">Flexible<br>Online Payment<br>Options</span></div>
  <div class="divider" style="left:194px;top:315px"></div>
  <div class="feature" style="left:144px;top:331px"><span class="feature__icon" role="img" aria-label="Debt negotiation icon"></span><span class="feature__text">Online<br>Consumer<br>Debt Negotiating<br>Tools</span></div>
  <div class="divider" style="left:210px;top:410px"></div>
  <div class="feature" style="left:144px;top:421px"><span class="feature__icon" role="img" aria-label="Live chat agent icon"></span><span class="feature__text">Live Online<br>Agent Chat<br>Portals</span></div>
  <div class="divider" style="left:200px;top:497px"></div>
  <div class="feature" style="left:110px;top:506px"><span class="feature__icon" role="img" aria-label="Dispute tools icon"></span><span class="feature__text">Online Dispute<br>/Complaint<br>Tools</span></div>
  <div class="feature" style="left:26px;top:570px"><span class="feature__icon" role="img" aria-label="Compliance document icon"></span><span class="feature__text">FCRA/TCPA/FDCPA<br>Compliant</span></div>

  <h2 class="services section-title">Our<br>Services</h2>
  <div class="services__rule"></div>
  <ul class="service-list">
    <li><svg class="tick" viewBox="0 0 10 10"><circle cx="5" cy="5" r="5" fill="var(--teal)"/><path d="M2.8,5.2 4.4,6.7 7.3,3.6" stroke="#fff" stroke-width="1.3" fill="none"/></svg>Account Data Scrubbing</li>
    <li><svg class="tick" viewBox="0 0 10 10"><circle cx="5" cy="5" r="5" fill="var(--teal)"/><path d="M2.8,5.2 4.4,6.7 7.3,3.6" stroke="#fff" stroke-width="1.3" fill="none"/></svg>Collection Letters</li>
    <li><svg class="tick" viewBox="0 0 10 10"><circle cx="5" cy="5" r="5" fill="var(--teal)"/><path d="M2.8,5.2 4.4,6.7 7.3,3.6" stroke="#fff" stroke-width="1.3" fill="none"/></svg>Progressive Collection Calls</li>
    <li><svg class="tick" viewBox="0 0 10 10"><circle cx="5" cy="5" r="5" fill="var(--teal)"/><path d="M2.8,5.2 4.4,6.7 7.3,3.6" stroke="#fff" stroke-width="1.3" fill="none"/></svg>Multiple Credit Bureau Reporting</li>
    <li><svg class="tick" viewBox="0 0 10 10"><circle cx="5" cy="5" r="5" fill="var(--teal)"/><path d="M2.8,5.2 4.4,6.7 7.3,3.6" stroke="#fff" stroke-width="1.3" fill="none"/></svg>Payment Propensity Scoring</li>
    <li><svg class="tick" viewBox="0 0 10 10"><circle cx="5" cy="5" r="5" fill="var(--teal)"/><path d="M2.8,5.2 4.4,6.7 7.3,3.6" stroke="#fff" stroke-width="1.3" fill="none"/></svg>In Depth Skip Tracing</li>
    <li><svg class="tick" viewBox="0 0 10 10"><circle cx="5" cy="5" r="5" fill="var(--teal)"/><path d="M2.8,5.2 4.4,6.7 7.3,3.6" stroke="#fff" stroke-width="1.3" fill="none"/></svg>Life Cycle Monitoring</li>
    <li><svg class="tick" viewBox="0 0 10 10"><circle cx="5" cy="5" r="5" fill="var(--teal)"/><path d="M2.8,5.2 4.4,6.7 7.3,3.6" stroke="#fff" stroke-width="1.3" fill="none"/></svg>Deceased Audit/Probate Filing</li>
    <li><svg class="tick" viewBox="0 0 10 10"><circle cx="5" cy="5" r="5" fill="var(--teal)"/><path d="M2.8,5.2 4.4,6.7 7.3,3.6" stroke="#fff" stroke-width="1.3" fill="none"/></svg>Call Recording</li>
    <li><svg class="tick" viewBox="0 0 10 10"><circle cx="5" cy="5" r="5" fill="var(--teal)"/><path d="M2.8,5.2 4.4,6.7 7.3,3.6" stroke="#fff" stroke-width="1.3" fill="none"/></svg>Back End Legal Services</li>
    <li><svg class="tick" viewBox="0 0 10 10"><circle cx="5" cy="5" r="5" fill="var(--teal)"/><path d="M2.8,5.2 4.4,6.7 7.3,3.6" stroke="#fff" stroke-width="1.3" fill="none"/></svg>Bankruptcy Management</li>
  </ul>

  <div class="call">
    <span class="call__badge"><svg width="20" height="20" viewBox="0 0 24 24"><path d="M6.6 10.8a15 15 0 0 0 6.6 6.6l2.2-2.2a1 1 0 0 1 1-.25 11.4 11.4 0 0 0 3.6.57 1 1 0 0 1 1 1V20a1 1 0 0 1-1 1A17 17 0 0 1 3 4a1 1 0 0 1 1-1h3.5a1 1 0 0 1 1 1c0 1.25.2 2.45.57 3.57a1 1 0 0 1-.25 1z" fill="var(--teal)"/></svg></span>
    <span><span class="call__label">CALL US AT</span><br><span class="call__number">(555) 014-2290</span></span>
  </div>
  <div class="site">www.northgaterecovery.com</div>
</section>

<section class="flyer flyer--philosophy">
  <svg class="flyer__art" width="528" height="683" viewBox="0 0 528 683">
    <defs>
      <linearGradient id="stormSky" x1="0" y1="0" x2="1" y2="1">
        <stop offset="0" stop-color="var(--storm-a)"/>
        <stop offset="1" stop-color="var(--storm-b)"/>
      </linearGradient>
    </defs>
    <rect width="528" height="440" fill="url(#stormSky)" role="img" aria-label="Photo of a lit power transmission tower under a lightning storm"/>
    <path d="M0,205 C130,195 220,250 290,315 C240,290 150,265 0,275Z" fill="#e9eef2"/>
    <path d="M0,222 C140,210 225,258 300,330 C250,305 160,275 0,282Z" fill="var(--teal)"/>
    <path d="M0,278 C150,270 240,310 300,340 C360,370 410,372 460,360 C495,352 515,370 528,398 L528,683 L0,683Z" fill="var(--white)"/>
    <path d="M240,305 C300,360 360,380 420,370 C370,372 320,360 240,305Z" fill="var(--dark)"/>
    <g fill="var(--white)">
      <rect x="410" y="342" width="15" height="40"/>
      <rect x="433" y="320" width="15" height="62"/>
      <rect x="456" y="300" width="15" height="82"/>
      <rect x="479" y="278" width="15" height="104"/>
      <rect x="502" y="256" width="15" height="150"/>
    </g>
    <path d="M0,683 L0,672 C160,660 300,620 528,596 L528,683Z" fill="var(--dark)"/>
    <path d="M110,668 C200,660 260,640 300,632 C250,650 180,664 110,668Z" fill="var(--blue)"/>
    <path d="M222,412 H480 a10,10 0 0 1 10,10 V532 a10,10 0 0 1 -10,10 H50" fill="none" stroke="var(--teal)" stroke-width="1.2"/>
    <circle cx="222" cy="412" r="3" fill="var(--teal)"/>
    <circle cx="50" cy="542" r="3" fill="var(--teal)"/>
  </svg>

  <div class="brand"><span class="brand__dot"></span><span class="brand__name">NORTHGATE<br>RECOVERY</span></div>

  <h2 class="philosophy__title">Our<br>Philosophy</h2>
  <p class="philosophy__body">Utility collections pose a significant challenge simply because they are one of the<br>last bills to go unpaid during difficult financial times. When an individual’s utilities<br>are shut off, tough financial choices are having to be made. While this might not be<br>the case in every situation, a compassionate approach is always the best way to<br>begin working towards a resolution. Our agency has worked with utility companies<br>for over 30 years and our experience and long-term approach have proven to yield<br>the highest returns.</p>

  <div class="call">
    <span class="call__badge"><svg width="20" height="20" viewBox="0 0 24 24"><path d="M6.6 10.8a15 15 0 0 0 6.6 6.6l2.2-2.2a1 1 0 0 1 1-.25 11.4 11.4 0 0 0 3.6.57 1 1 0 0 1 1 1V20a1 1 0 0 1-1 1A17 17 0 0 1 3 4a1 1 0 0 1 1-1h3.5a1 1 0 0 1 1 1c0 1.25.2 2.45.57 3.57a1 1 0 0 1-.25 1z" fill="var(--teal)"/></svg></span>
    <span><span class="call__label">CALL US AT</span><br><span class="call__number">(555) 014-2290</span></span>
  </div>
  <div class="site">www.northgaterecovery.com</div>
</section>

</body>
</html>
```